Business Card Design - Corporate

Create a sleek elegant business card layout while suggesting a color scheme. Convey cutting edge technology while maintaining a corporate feel that is easily readable.

Company designs and manufactures consumer electronic products for mass retail that are mainly app driven.

(vector logo and die-line provided)

Target Market(s)

Corporate level, tech industry.

Industry/Entity Type

Business

Contact Information for Business Card

Generic Info:

Name
Title
email
address
phone 1
phone 2
website (quillbarn.com) on back

Font styles to use
Sans Serif

Requirements
Must have
• At least 2 colors + white on one side.
Nice to have
• Solid suggestion on color for logo and overall design. Color flood on back of card.
Should not have
• background texture like... marble, stone, patterns or circuit boards

```html
<!DOCTYPE html>
<html lang="en">
<head>
<meta charset="utf-8">
<title>Quillbarn Business Card</title>
<link href="https://fonts.googleapis.com/css2?family=Montserrat:wght@400;500;700&display=swap" rel="stylesheet">
<style>
  :root {
    --backdrop: #2b2320;
    --ink: #161616;
    --card-dark: #1b1b1b;
    --paper: #ffffff;
    --accent: #e5202e;
    --silver: #c9c9c9;
    --text: #2a2a2a;
  }
  * { box-sizing: border-box; margin: 0; padding: 0; }
  html, body { width: 1200px; height: 1000px; overflow: hidden; }
  body {
    background: var(--backdrop);
    font-family: "Montserrat", Arial, sans-serif;
    position: relative;
  }
  .card {
    position: absolute;
    left: 330px;
    width: 540px;
    height: 310px;
    border-radius: 24px;
    overflow: hidden;
    box-shadow: 0 10px 24px rgba(0,0,0,0.45);
  }
  .card-front { top: 150px; background: var(--paper); }
  .card-back { top: 540px; background: var(--card-dark); }

  .front-dark-panel {
    position: absolute; left: 0; top: 0;
    width: 220px; height: 100%;
    background: var(--card-dark);
  }
  .front-wordmark {
    position: absolute; left: 26px; top: 34px;
    color: var(--silver);
    font-weight: 500;
    font-size: 19px;
    letter-spacing: 2px;
  }
  .rocket-illustration {
    position: absolute; left: 178px; top: 30px;
    width: 84px; height: 262px;
    border-radius: 42px 42px 10px 10px;
    background: linear-gradient(90deg, var(--ink) 0%, var(--ink) 50%, #e9e9e9 50%, #d4d4d4 100%);
  }
  .contact-block {
    position: absolute; left: 300px; top: 96px;
    color: var(--text);
  }
  .person-name {
    font-weight: 700; font-size: 21px; color: var(--ink);
    letter-spacing: 0.3px;
  }
  .person-name .surname { color: var(--accent); }
  .person-title { font-size: 14px; margin-top: 4px; margin-bottom: 16px; }
  .contact-line {
    display: flex; align-items: flex-start; gap: 9px;
    font-size: 13px; line-height: 17px; margin-bottom: 3px;
  }
  .contact-line svg { flex: none; margin-top: 2px; }
  .contact-line.address { margin-top: 5px; }

  .back-wordmark {
    position: absolute; left: 0; right: 0; top: 112px;
    text-align: center;
    color: var(--silver);
    font-weight: 500;
    font-size: 46px;
    letter-spacing: 3px;
  }
  .back-rule {
    position: absolute; left: 62px; top: 180px;
    width: 416px; height: 3px;
    background: var(--accent);
  }
</style>
</head>
<body>
  <section class="card card-front">
    <div class="front-dark-panel"></div>
    <div class="front-wordmark">QUILLBARN</div>
    <div class="rocket-illustration" role="img" aria-label="Black and white rocket illustration"></div>
    <div class="contact-block">
      <div class="person-name">JOHN <span class="surname">DOE</span></div>
      <div class="person-title">Principal</div>
      <div class="contact-line">
        <svg width="13" height="12" viewBox="0 0 24 24"><path fill="#e5202e" d="M6.6 10.8a15 15 0 0 0 6.6 6.6l2.2-2.2a1 1 0 0 1 1-.25 11.4 11.4 0 0 0 3.6.57 1 1 0 0 1 1 1V20a1 1 0 0 1-1 1A17 17 0 0 1 3 4a1 1 0 0 1 1-1h3.5a1 1 0 0 1 1 1c0 1.25.2 2.45.57 3.6a1 1 0 0 1-.25 1z"/></svg>
        <span>123 456 7890</span>
      </div>
      <div class="contact-line">
        <svg width="13" height="12" viewBox="0 0 24 24"><path fill="#e5202e" d="M6.6 10.8a15 15 0 0 0 6.6 6.6l2.2-2.2a1 1 0 0 1 1-.25 11.4 11.4 0 0 0 3.6.57 1 1 0 0 1 1 1V20a1 1 0 0 1-1 1A17 17 0 0 1 3 4a1 1 0 0 1 1-1h3.5a1 1 0 0 1 1 1c0 1.25.2 2.45.57 3.6a1 1 0 0 1-.25 1z"/></svg>
        <span>123 466 7897</span>
      </div>
      <div class="contact-line">
        <svg width="13" height="12" viewBox="0 0 24 20"><path fill="#e5202e" d="M2 2h20a2 2 0 0 1 2 2v.5L12 11 0 4.5V4a2 2 0 0 1 2-2zm-2 5 12 6.5L24 7v10a2 2 0 0 1-2 2H2a2 2 0 0 1-2-2z"/></svg>
        <span>youremail@domain.com</span>
      </div>
      <div class="contact-line address">
        <svg width="13" height="14" viewBox="0 0 24 24"><path fill="#e5202e" d="M12 2a7 7 0 0 0-7 7c0 5 7 13 7 13s7-8 7-13a7 7 0 0 0-7-7zm0 9.5A2.5 2.5 0 1 1 12 6.5a2.5 2.5 0 0 1 0 5z"/></svg>
        <span>2741 Alder Crest Lane<br>Marlow, OR 97220</span>
      </div>
    </div>
  </section>

  <section class="card card-back">
    <div class="back-wordmark">quillbarn.com</div>
    <div class="back-rule"></div>
  </section>
</body>
</html>
```